Gratefl Moments/Coral Friday

Create a double sided postcard which will be distributed to 60,000 destinations, suitable for printing on re-cycled card.

Promotional offer ends Sunday August 31st 2014

It is Winter in Perth Western Australia, colours need to be bright and a reminder of summer. The card needs to be fun with a Mediterranean Spanish type feel
web site www.kelvport.com.au

```html
<!DOCTYPE html>
<html lang="en">
<head>
<meta charset="utf-8">
<title>Coral Friday Postcard</title>
<link href="https://fonts.googleapis.com/css2?family=Roboto:wght@300;400&family=Roboto+Condensed:wght@400&family=Arimo:wght@700&display=swap" rel="stylesheet">
<style>
:root{
  --bg:#e9e6e1;
  --card:#ffffff;
  --blue:#1d5ea8;
  --blue-deep:#1a4f92;
  --ink:#1e1e1e;
  --ink-soft:#333333;
  --line:#555555;
  --stamp:#111111;
}
*{margin:0;padding:0;box-sizing:border-box}
html,body{width:808px;height:1200px;overflow:hidden;background:var(--bg)}
.stage{position:relative;width:808px;height:1200px}
.card{position:absolute;left:52px;width:703px;background:var(--card);box-shadow:0 2px 6px rgba(0,0,0,.25);overflow:hidden}
.card--front{top:38px;height:544px}
.card--back{top:615px;height:545px}
.front-art{position:absolute;left:0;top:0;width:703px;height:467px}
.front-copy{position:absolute;left:20px;top:22px;color:var(--ink);font-family:'Roboto',Arial,sans-serif}
.front-title{font-weight:300;font-size:25px;line-height:31px}
.front-intro{font-family:'Roboto Condensed',Arial Narrow,sans-serif;font-size:13px;line-height:19px;margin-top:6px;color:var(--ink-soft)}
.plate-title{font-weight:300;font-size:28px;line-height:32px;margin-top:52px}
.plate-price{font-family:'Arimo',Arial,sans-serif;font-weight:700;font-size:35px;margin-top:22px;letter-spacing:-.5px}
.plate-price span{font-family:'Roboto',Arial,sans-serif;font-weight:300}
.plate-items{font-family:'Roboto Condensed',Arial Narrow,sans-serif;font-size:13px;line-height:24px;margin-top:20px;color:var(--ink-soft)}
.footer{position:absolute;left:0;bottom:0;width:703px;height:77px;background:var(--card)}
.brand{position:absolute;left:20px;top:6px;width:118px;height:58px;background:var(--blue);display:flex;align-items:center;justify-content:center;gap:6px}
.brand-name{font-family:'Roboto',Arial,sans-serif;font-weight:400;font-size:10px;letter-spacing:1.5px;color:#fff}
.brand-mark{width:7px;height:7px;border-radius:50%;background:#fff}
.footer-address{position:absolute;left:150px;top:6px;font-family:'Roboto Condensed',Arial Narrow,sans-serif;font-size:16px;color:var(--ink)}
.footer-bookings{position:absolute;left:150px;top:30px;font-family:'Roboto',Arial,sans-serif;font-weight:300;font-size:24px;color:var(--ink)}
.back-header{position:absolute;left:0;top:0;width:530px;height:175px;background:var(--blue);color:#fff;text-align:center;font-family:'Roboto',Arial,sans-serif}
.back-headline{font-weight:300;font-size:26px;line-height:36px;margin-top:12px}
.back-price{font-family:'Arimo',Arial,sans-serif;font-weight:700;font-size:33px;margin-top:6px}
.back-hours{font-weight:300;font-size:16px;margin-top:12px}
.stamp-box{position:absolute;left:538px;top:23px;width:138px;height:142px;background:var(--stamp)}
.menu{position:absolute;left:0;top:185px;width:353px;text-align:center;font-family:'Roboto Condensed',Arial Narrow,sans-serif;font-size:11px;line-height:14px;color:var(--ink)}
.divider-v{position:absolute;left:353px;top:175px;width:1px;height:288px;background:var(--line)}
.divider-h{position:absolute;left:0;top:463px;width:703px;height:1px;background:var(--line)}
.address-lines{position:absolute;left:420px;top:260px;font-family:'Roboto Condensed',Arial Narrow,sans-serif;font-size:11px;color:var(--ink)}
.address-line{position:absolute;left:23px;width:190px;border-bottom:1px solid var(--line)}
.card--back .footer{height:82px}
</style>
</head>
<body>
<div class="stage">

  <section class="card card--front">
    <svg class="front-art" viewBox="0 0 703 467" role="img" aria-label="Harbour view with moored yachts and city skyline, a grilled snapper fillet on sweetcorn, and bowls of seafood noodle soup">
      <defs>
        <linearGradient id="harbour" x1="0" y1="0" x2="0" y2="1">
          <stop offset="0" stop-color="#f3f4f6"/>
          <stop offset=".55" stop-color="#dde1e6"/>
          <stop offset="1" stop-color="#eef0f2"/>
        </linearGradient>
        <radialGradient id="dish" cx=".62" cy=".55" r=".6">
          <stop offset="0" stop-color="#d9b48a"/>
          <stop offset=".45" stop-color="#e8a634"/>
          <stop offset="1" stop-color="#f3f1ee"/>
        </radialGradient>
        <radialGradient id="bowls" cx=".5" cy=".5" r=".6">
          <stop offset="0" stop-color="#f1ebe0"/>
          <stop offset=".7" stop-color="#d9c9b4"/>
          <stop offset="1" stop-color="#8a7a68"/>
        </radialGradient>
      </defs>
      <rect width="703" height="467" fill="url(#harbour)"/>
      <path d="M462 0 C350 60 300 220 318 467 L703 467 L703 0 Z" fill="var(--blue)"/>
      <path d="M490 0 C385 70 335 230 352 467 L703 467 L703 0 Z" fill="url(#dish)"/>
      <ellipse cx="366" cy="402" rx="142" ry="82" fill="var(--blue)"/>
      <ellipse cx="370" cy="404" rx="132" ry="74" fill="url(#bowls)"/>
    </svg>

    <div class="front-copy">
      <h1 class="front-title">Celebrate<br>Coral Friday's</h1>
      <p class="front-intro">Celebrate Sunday's on Perth's most beautiful<br>bay with a selection of magnificent<br>Western Australian seafood, from Shark Bay.</p>
      <h2 class="plate-title">Coral Friday<br>Plate</h2>
      <p class="plate-price">$38.00<span>pp</span></p>
      <p class="plate-items">Grilled Scampi, Prawns,<br>Cuttlefish, Pink Snapper<br>and Scallops</p>
    </div>

    <footer class="footer">
      <div class="brand"><span class="brand-name">HARBOURLIGHT</span><span class="brand-mark"></span></div>
      <p class="footer-address">Harbourlight Restaurant and Function Centre 12 Tidewater Drive Marlow 6001</p>
      <p class="footer-bookings">Bookings w: www.kelvport.com.au p 9555-0142</p>
    </footer>
  </section>

  <section class="card card--back">
    <header class="back-header">
      <h1 class="back-headline">Gratefl Moments with Lunch overlooking<br>Perth's most beautiful Bay</h1>
      <p class="back-price">$48.00 per person</p>
      <p class="back-hours">(Available Monday to Friday 11am until 3pm)</p>
    </header>
    <div class="stamp-box"></div>

    <div class="menu">
      <p>Select one dish from each course with your choice of either a glass<br>of Villa Corvo Soave 2011 or Monte Rosa Valpolicella Classico 2011</p>
      <p>Freshly baked Italian style crusty bread,</p>
      <p>Entrée</p>
      <p>Passionfruit and citrus cured Tasmanian salmon</p>
      <p>or</p>
      <p>Pork belly, marinated, horseradish coleslaw</p>
      <p>or</p>
      <p>Welsh rarebit, sautéed mushrooms, hot English mustard mayo</p>
      <p>or</p>
      <p>Fried squid, tubes, cannellini pure, green chilli sauce</p>
      <p>Main</p>
      <p>Pink snapper fillet, grilled, xo sauce, kim chi</p>
      <p>or</p>
      <p>Wagyu rump, served with cauliflower puree, broad beans</p>
      <p>or</p>
      <p>Soft polenta, grilled haloumi, crusted eggplant, red pepper coulis</p>
      <p>or</p>
      <p>Confit duck leg caramelised red onion, grilled manchego stuffed fig</p>
    </div>
    <div class="divider-v"></div>

    <div class="address-lines">
      <span>To,</span>
      <span class="address-line" style="top:13px"></span>
      <span class="address-line" style="top:45px"></span>
      <span class="address-line" style="top:79px"></span>
      <span class="address-line" style="top:111px"></span>
    </div>

    <div class="divider-h"></div>
    <footer class="footer">
      <div class="brand" style="top:10px"><span class="brand-name">HARBOURLIGHT</span><span class="brand-mark"></span></div>
      <p class="footer-address" style="top:8px">Harbourlight Restaurant and Function Centre 12 Tidewater Drive Marlow 6001</p>
      <p class="footer-bookings" style="top:32px">Bookings w: www.kelvport.com.au p 9555-0142</p>
    </footer>
  </section>

</div>
</body>
</html>
```